" É uma empresa de consultoria e assessoria em engenharia ambiental, que trabalha com assistência técnica a advogados criminais. Também trabalha com licenciamento ambiental "

```html
<!DOCTYPE html>
<html lang="pt-BR">
<head>
<meta charset="UTF-8">
<title>Vertente – Pasta de Documentos</title>
<link href="https://fonts.googleapis.com/css2?family=Marcellus&family=Montserrat:wght@400;500;600&display=swap" rel="stylesheet">
<style>
  :root {
    --bg: #bdbdbd;
    --paper: #ffffff;
    --forest: #1f4f4a;
    --leaf: #8fbf7f;
    --leaf-light: #a9d19a;
    --faint: #eef3ec;
    --ink: #3a3a3a;
    --label: #222222;
  }
  * { margin: 0; padding: 0; box-sizing: border-box; }
  html, body { width: 1200px; height: 1200px; overflow: hidden; }
  body {
    background: var(--bg);
    position: relative;
    font-family: "Montserrat", sans-serif;
  }
  .sheet-label {
    position: absolute; left: 24px; top: 24px;
    font-size: 19px; color: var(--label); letter-spacing: 0.5px;
  }
  .folder-pocket { position: absolute; left: 0; top: 0; }
  .panel { position: absolute; top: 96px; height: 703px; }
  .panel-back { left: 240px; width: 389px; background: var(--paper); }
  .panel-front { left: 629px; width: 355px; background: var(--forest); }
  .back-decoration {
    position: absolute; left: 40px; top: 140px;
    width: 230px; height: 230px; border-radius: 50%;
    background: var(--faint);
  }
  .back-brand {
    position: absolute; left: 0; right: 0; top: 590px; text-align: center;
  }
  .back-brand .name {
    font-family: "Marcellus", serif; font-size: 24px; color: var(--forest);
    letter-spacing: 3px; line-height: 1;
  }
  .back-brand .tagline {
    font-size: 5.5px; color: var(--forest); letter-spacing: 1px; margin-top: 3px;
  }
  .contacts {
    position: absolute; left: 36px; right: 36px; top: 645px;
    display: grid; grid-template-columns: 1fr 1fr 1.3fr; gap: 4px 14px;
    font-size: 7px; color: var(--ink);
  }
  .contacts span::before {
    content: ""; display: inline-block; width: 5px; height: 5px;
    border-radius: 50%; background: var(--leaf); margin-right: 4px;
  }
  .front-brand {
    position: absolute; left: 0; right: 0; top: 390px; text-align: center;
  }
  .front-brand .name {
    font-family: "Marcellus", serif; font-size: 50px; color: var(--paper);
    letter-spacing: 4px; line-height: 1;
  }
  .front-brand .tagline {
    font-size: 13px; font-weight: 500; color: var(--leaf-light);
    letter-spacing: 1.5px; line-height: 1.45; margin-top: 8px;
  }
  .pocket-edge {
    position: absolute; left: 684px; top: 792px; width: 300px; height: 14px;
    background: var(--leaf); border-radius: 8px 8px 0 0;
  }
</style>
</head>
<body>
  <div class="sheet-label">PASTA DE DOCUMENTOS</div>

  <section class="panel panel-back">
    <div class="back-decoration" aria-hidden="true"></div>
    <div class="back-brand">
      <div class="name">VERTENTE</div>
      <div class="tagline">CONSULTORIA E ASSESSORIA INTEGRADA</div>
    </div>
    <div class="contacts">
      <span>(11) 4000-0000</span>
      <span>contato@vertente.com</span>
      <span>Rua das Palmeiras, 120 – Centro</span>
      <span>@vertenteambiental</span>
      <span>www.vertente.com</span>
      <span>CEP 00000-000 – Cidade</span>
    </div>
  </section>

  <section class="panel panel-front">
    <div class="front-brand">
      <div class="name">VERTENTE</div>
      <div class="tagline">CONSULTORIA E ASSESSORIA<br>INTEGRADA</div>
    </div>
  </section>

  <div class="pocket-edge" aria-hidden="true"></div>

  <svg class="folder-pocket" width="1200" height="1200" viewBox="0 0 1200 1200" aria-hidden="true">
    <path d="M144 805 L180 799 L180 1068 L150 1058 L144 1040 Z" fill="#ffffff"/>
    <path d="M180 799 L629 799 L629 924 C520 930 430 960 360 1010 C300 1050 240 1068 180 1068 Z" fill="#8fbf7f"/>
    <line x1="206" y1="850" x2="242" y2="886" stroke="#ffffff" stroke-width="2"/>
    <line x1="214" y1="922" x2="262" y2="948" stroke="#ffffff" stroke-width="2"/>
  </svg>
</body>
</html>
```